Web design for upcoming direct placement agency

So were looking for a very modern, simple but professional look. We would like to have the site able to translate into 4 different languages- a few idea sites you can reference would be
www.lorvanteam.com **our favorite**
www.brightmeadowfolk.org

We want to ensure the website is tailored to both our clients as well as potential candidates. We want our clients and candidates to understand that we are dedicated to making sure that we want to build relationships with them and that we want to do everything possible to make sure they succeed.

We'd like to steer away from too many up close photos of people. Instead you could try a shadowed view or distant photo that limits the directness.

we have a domain name- www.talvinharbourllc.com

We will upload our business plan as well as a sample business proposal so you have an idea of the information we would like to include.

Target Market(s)

Business' looking to outsource their hiring needs for upper level positions such as but not limited to quality engineers, logistics managers, material managers, etc

Industry/Entity Type

Employment Agency

Number of Pages Required

3 page

Font styles to use
Serif
Sans Serif
Script
Other font styles liked:
• Kennedy Sm Caps

Colors
1b1b1b
9d9d9d
e9e9e9
eeeeee
dadada
0255a3
85acd3
474747

Requirements
Must have
• -ability to translate to English, Spanish, German, and Japanese.
• -Our logo
• -A contact us section
• -Resume upload area
Should not have
• -A job search area
• -pricing info

```html
<!DOCTYPE html>
<html lang="en">
<head>
<meta charset="utf-8">
<title>Talvin Harbour – Direct Placement</title>
<link href="https://fonts.googleapis.com/css2?family=Cinzel:wght@400;700&family=Lora:ital,wght@0,400;0,700;1,400&family=Open+Sans:wght@400;600;700&display=swap" rel="stylesheet">
<style>
:root{
  --navy:#1d3a63;
  --blue:#0255a3;
  --blue-mid:#2b62a3;
  --blue-light:#85acd3;
  --ink:#1b1b1b;
  --ink-soft:#474747;
  --grey:#9d9d9d;
  --line:#dadada;
  --paper:#eeeeee;
  --paper-2:#e9e9e9;
  --white:#ffffff;
}
*{box-sizing:border-box;margin:0;padding:0}
html,body{width:1200px;height:2340px;overflow:hidden}
body{font-family:"Open Sans",Arial,sans-serif;color:var(--ink-soft);background:var(--white)}
.page{width:1200px;height:2340px;position:relative}

.topbar{height:38px;background:var(--navy);color:var(--white);display:flex;align-items:center;justify-content:space-between;padding:0 30px;font-size:13px}
.topbar .contact{display:flex;gap:26px;align-items:center}
.topbar .contact span{display:flex;align-items:center;gap:7px;font-weight:600}
.topbar .tools{display:flex;gap:8px;align-items:center}
.dot{width:20px;height:20px;border-radius:50%;background:var(--blue-mid)}
.lang{margin-left:10px;border:1px solid var(--blue-light);padding:1px 8px;font-size:12px}

.header{height:62px;display:flex;align-items:center;justify-content:space-between;padding:0 30px;border-bottom:1px solid var(--line)}
.brand{display:flex;align-items:center;gap:10px;font-family:"Lora",serif;font-weight:700;color:var(--blue);font-size:22px}
.brand .mark{width:30px;height:30px;border-radius:50%;background:var(--blue)}
.nav{display:flex;gap:6px}
.nav a{font-size:13px;color:var(--ink);text-decoration:none;padding:8px 13px;border-radius:2px}
.nav a.active{background:var(--navy);color:var(--white)}

.hero{height:550px;position:relative;background:linear-gradient(180deg,#cfd4d9 0%,#a9b1b9 55%,#6e7780 100%);color:var(--white)}
.hero .welcome{position:absolute;left:60px;top:250px}
.hero h1{font-family:"Lora",serif;font-weight:400;font-size:62px;line-height:1}
.hero p{font-family:"Lora",serif;font-size:26px;margin-top:20px}
.hero .actions{display:flex;gap:16px;margin-top:26px}
.btn-hero{background:var(--navy);color:var(--white);font-size:15px;padding:12px 22px;width:170px;display:flex;justify-content:space-between;align-items:center}

.section-title{font-family:"Cinzel",serif;text-align:center;font-size:32px;color:var(--ink);letter-spacing:1px}
.section-title b{color:var(--blue)}
.rule{width:420px;height:1px;background:var(--line);margin:10px auto 0}

.about{height:310px;padding-top:40px;text-align:center}
.about .text{width:1080px;margin:28px auto 0;font-size:12.5px;line-height:1.8;color:var(--ink-soft)}
.btn{display:inline-block;background:var(--blue);color:var(--white);font-size:13px;padding:9px 22px;border-radius:2px;margin-top:26px}

.services{height:530px;background:var(--blue-mid);padding-top:44px;color:var(--white);position:relative}
.services .section-title{color:var(--white)}
.services .rule{background:var(--blue-light)}
.cards{display:flex;justify-content:center;gap:40px;margin-top:40px}
.card{width:235px;text-align:center}
.circle{width:120px;height:120px;border:3px solid var(--white);border-radius:50%;margin:0 auto;display:flex;align-items:center;justify-content:center}
.card h3{font-family:"Lora",serif;font-weight:400;font-size:26px;margin-top:18px}
.card p{font-size:12px;line-height:1.6;margin-top:10px}
.card .btn{background:var(--white);color:var(--blue);margin-top:18px}
.chevron{position:absolute;left:50%;bottom:-22px;transform:translateX(-50%);width:44px;height:44px;background:var(--white);border-radius:50%;display:flex;align-items:center;justify-content:center}

.lower{height:320px;background:var(--paper);display:flex;padding:50px 40px 0}
.blog{width:720px}
.lower h2{font-family:"Cinzel",serif;font-size:28px;color:var(--ink);border-bottom:1px solid var(--line);padding-bottom:8px}
.lower h2 b{color:var(--blue)}
.posts{display:flex;gap:24px;margin-top:22px}
.post{width:210px}
.post .thumb{height:120px;background:linear-gradient(135deg,#8fb3d6,#d9e4ef)}
.post .cap{font-size:12px;color:var(--ink);margin-top:8px}
.post .date{font-size:11px;color:var(--blue);margin-top:2px}
.testi{width:380px;margin-left:40px}
.quote{background:var(--white);border:1px solid var(--line);padding:16px;margin-top:22px;font-size:12px;line-height:1.6;color:var(--ink-soft)}
.person{display:flex;align-items:center;gap:10px;margin-top:14px;font-size:12px}
.person .av{width:40px;height:40px;border-radius:50%;background:var(--line)}
.person b{color:var(--blue);display:block}

.newsletter{height:120px;display:flex;align-items:center;padding:0 40px;gap:18px;border-top:1px solid var(--line)}
.newsletter h2{font-family:"Cinzel",serif;font-size:30px;color:var(--ink)}
.newsletter h2 b{color:var(--blue)}
.newsletter small{display:block;font-size:11px;color:var(--grey)}
.newsletter .field{margin-left:auto;width:440px;height:40px;border:1px solid var(--line);font-size:12px;color:var(--grey);padding:11px 14px}
.newsletter .btn{margin-top:0;padding:11px 36px}

.footer{height:370px;background:var(--ink);color:var(--grey);display:flex;padding:36px 40px 0;gap:40px;font-size:12px}
.footer h4{color:var(--white);font-size:14px;letter-spacing:1px;border-bottom:1px solid var(--ink-soft);padding-bottom:8px;margin-bottom:14px}
.col-links{width:200px}
.col-links li{list-style:none;padding:7px 0;border-bottom:1px solid #2a2a2a}
.col-links li:first-child{color:var(--white)}
.col-contact{width:260px;line-height:1.8}
.col-contact b{color:var(--white)}
.col-map{width:300px}
.map{height:180px;background:linear-gradient(135deg,#d8d8d8,#bdbdbd)}
.col-follow{width:200px}
.social{display:flex;align-items:center;gap:12px;margin-bottom:16px}
.social .dot{width:32px;height:32px;background:var(--blue)}
.social b{color:var(--white);display:block;font-size:12px}
.copyright{height:40px;background:#111;color:var(--grey);font-size:11px;display:flex;align-items:center;justify-content:center}
</style>
</head>
<body>
<div class="page">

  <div class="topbar">
    <div class="contact">
      <span><svg width="12" height="12" viewBox="0 0 24 24" fill="#fff"><path d="M6.6 10.8a15 15 0 0 0 6.6 6.6l2.2-2.2c.3-.3.7-.4 1-.2 1.1.4 2.3.6 3.6.6.6 0 1 .4 1 1V20c0 .6-.4 1-1 1A17 17 0 0 1 3 4c0-.6.4-1 1-1h3.5c.6 0 1 .4 1 1 0 1.3.2 2.5.6 3.6.1.3 0 .7-.2 1z"/></svg>(555) 210-3876</span>
      <span><svg width="13" height="10" viewBox="0 0 26 20" fill="none" stroke="#fff" stroke-width="2"><rect x="1" y="1" width="24" height="18"/><path d="M1 1l12 10L25 1"/></svg>info@talvinharbourllc.com</span>
    </div>
    <div class="tools"><span class="dot"></span><span class="dot"></span><span class="dot"></span><span class="dot"></span><span class="lang">ENG ▾</span></div>
  </div>

  <div class="header">
    <div class="brand"><span class="mark"></span>Talvin Harbour</div>
    <nav class="nav"><a class="active">Home</a><a>About Us</a><a>Services</a><a>Jobs</a><a>Blog</a><a>Contact Us</a></nav>
  </div>

  <section class="hero" role="img" aria-label="Distant view of a businessman in a suit holding a briefcase, seen from behind, overlooking a grey city skyline">
    <div class="welcome">
      <h1>Welcome</h1>
      <p>Your Partner in Direct Placement</p>
      <div class="actions"><span class="btn-hero">Job Search <span>›</span></span><span class="btn-hero">Submit A CV <span>›</span></span></div>
    </div>
  </section>

  <section class="about">
    <h2 class="section-title"><b>About</b> Talvin Harbour</h2>
    <div class="rule"></div>
    <p class="text">We at Talvin Harbour partner with employers across manufacturing and engineering to place proven leaders in roles that matter. Our team studies every opening, learns the culture behind it and presents only candidates who fit both the work and the people. For candidates, we offer honest guidance, steady communication and access to positions that are rarely advertised. For clients, we cut the time and cost of hiring while raising the quality of every shortlist. We build lasting relationships on both sides because your success is the measure of ours, today and for years ahead.</p>
    <span class="btn">Read More</span>
  </section>

  <section class="services">
    <h2 class="section-title">Our Services</h2>
    <div class="rule"></div>
    <div class="cards">
      <div class="card">
        <div class="circle"><svg width="54" height="54" viewBox="0 0 24 24" fill="#fff"><circle cx="12" cy="7" r="4"/><path d="M4 21c0-4.4 3.6-7 8-7s8 2.6 8 7z"/></svg></div>
        <h3>Employment</h3>
        <p>Direct placement for quality engineers, logistics managers and material leaders matched to your exact needs and culture.</p>
        <span class="btn">Read More</span>
      </div>
      <div class="card">
        <div class="circle"><svg width="60" height="54" viewBox="0 0 28 24" fill="#fff"><circle cx="9" cy="7" r="3.5"/><circle cx="19" cy="7" r="3.5"/><path d="M2 20c0-3.8 3-6 7-6s7 2.2 7 6zM13 20c0-3.8 2-6 6-6s7 2.2 7 6z"/></svg></div>
        <h3>Recruiting</h3>
        <p>A focused search process that sources, screens and interviews candidates so your team meets only the strongest.</p>
        <span class="btn">Read More</span>
      </div>
      <div class="card">
        <div class="circle"><svg width="54" height="54" viewBox="0 0 24 24" fill="none" stroke="#fff" stroke-width="2"><circle cx="10" cy="10" r="6.5"/><path d="M15 15l6 6"/><path d="M7 12l2-2 2 1.5 2-3"/></svg></div>
        <h3>Market Analysis</h3>
        <p>Salary benchmarks and talent market insight that help you plan hires and make competitive offers with confidence.</p>
        <span class="btn">Read More</span>
      </div>
      <div class="card">
        <div class="circle"><svg width="54" height="54" viewBox="0 0 24 24" fill="none" stroke="#fff" stroke-width="2"><circle cx="12" cy="12" r="9"/><path d="M15 9c-.5-1-1.6-1.6-3-1.6-1.7 0-3 .9-3 2.2 0 3 6 1.6 6 4.6 0 1.3-1.3 2.3-3 2.3-1.5 0-2.7-.7-3.1-1.8M12 5.5v13"/></svg></div>
        <h3>Pricing</h3>
        <p>Clear, simple terms for every search with no hidden fees, so you always know what to expect.</p>
        <span class="btn">Read More</span>
      </div>
    </div>
    <div class="chevron"><svg width="18" height="12" viewBox="0 0 18 12" fill="none" stroke="#2b62a3" stroke-width="3"><path d="M2 2l7 7 7-7"/></svg></div>
  </section>

  <section class="lower">
    <div class="blog">
      <h2><b>Latest</b> Blog</h2>
      <div class="posts">
        <div class="post"><div class="thumb" role="img" aria-label="Photo of business people on a blue sky background"></div><p class="cap">Hiring leaders in manufacturing</p><p class="date">October 6, 2015</p></div>
        <div class="post"><div class="thumb" role="img" aria-label="Photo of a world map on a desk"></div><p class="cap">Hiring leaders in manufacturing</p><p class="date">October 6, 2015</p></div>
        <div class="post"><div class="thumb" role="img" aria-label="Photo of office chairs in a bright meeting room"></div><p class="cap">Hiring leaders in manufacturing</p><p class="date">October 6, 2015</p></div>
      </div>
    </div>
    <div class="testi">
      <h2><b>Client</b> Testimonial</h2>
      <div class="quote">Talvin Harbour found us a logistics manager in three weeks. Their team listened closely and every candidate was a strong fit.</div>
      <div class="person"><span class="av" role="img" aria-label="Client portrait placeholder"></span><span><b>Dana Whitfield</b>Operations Director</span></div>
    </div>
  </section>

  <section class="newsletter">
    <svg width="46" height="34" viewBox="0 0 26 20" fill="none" stroke="#0255a3" stroke-width="2"><rect x="1" y="1" width="24" height="18"/><path d="M1 1l12 10L25 1"/></svg>
    <div><h2><b>Newsletter</b> Signup</h2><small>Latest openings and hiring news monthly</small></div>
    <div class="field">Your email address</div>
    <span class="btn">Sign Up</span>
  </section>

  <footer class="footer">
    <div class="col-links"><h4>QUICK LINKS</h4><ul><li>Home</li><li>About Us</li><li>Services</li><li>Blog</li><li>Jobs</li><li>Contact Us</li></ul></div>
    <div class="col-contact"><h4>CONTACT INFORMATION</h4><p><b>TALVIN HARBOUR</b><br>1250 Harbour Point Drive, Suite 400, Greenville, SC 29601</p><p>(555) 210-3876</p><p>info@talvinharbourllc.com</p></div>
    <div class="col-map"><h4>LOCATION MAP</h4><div class="map" role="img" aria-label="Street map showing the office location"></div></div>
    <div class="col-follow"><h4>FOLLOW US</h4>
      <div class="social"><span class="dot"></span><span><b>COMMUNITY</b>Join us</span></div>
      <div class="social"><span class="dot"></span><span><b>NETWORK</b>Join us</span></div>
      <div class="social"><span class="dot"></span><span><b>UPDATES</b>Join us</span></div>
    </div>
  </footer>
  <div class="copyright">© 2015 Talvin Harbour. All Rights Reserved.</div>

</div>
</body>
</html>
```